SEO marketing site

I need a design only for an SEO/Marketing project I have in mind. I have bought the domain Brivvora.example and want to aim this project at businesses who want to push their business further. WHEN I SAY DESIGN ONLY, I MEAN NO PROGRAMMING. HOWEVER, I DO NEED THE DESIGNER TO PUT THIS SITE ONLINE. $300 IS A LOT OF MONEY FOR A TEMPLATE YOU CAN PURCHASE FOR $60 WITH SOME CUSTOMISATION.

The idea is that businesses will register with us and will be offered two different kinds of services. They can make use of our scripts to check their back links, rankings, compare with competitors and a number of other marketing tools. The other service we provide is that we offer them an SEO service at a very competitive price. We will handle social networking, link building, article submission, directory submission, social bookmarking etc etc at a reasonable monthly fee.

I qoros tram look/flat design is what I really like, and I want to give off a professional vibe. This is the kind of site I wish to go for.

JUST TO REPEAT, I NEED A DESIGN TO BE PUT ONLINE, I.E PSD TO HTML CONVERSION. MY PROGRAMMERS WILL CODE THE CLIENT AREA THEMSELVES.

Target Market(s)

Other businesses

Industry/Entity Type

Marketing

Requirements
Must have
• Qoros 8 or flat design look. Even a site, similar to makerhive, is quite attractive. I would like a killer design for the site.

```html
<!DOCTYPE html>
<html lang="en">
<head>
<meta charset="utf-8">
<title>Brivvora.example — SEO Marketing</title>
<link href="https://fonts.googleapis.com/css2?family=Open+Sans:wght@400;600&display=swap" rel="stylesheet">
<style>
:root{
  --accent:#1fa8e2;
  --btn:#3b8fe0;
  --btn-dark:#2b78c6;
  --green:#6cbf2a;
  --ink:#444;
  --ink-soft:#6a6a6a;
  --muted:#888;
  --hero:#3b3b3b;
  --hero-soft:#eaeaea;
  --band:#f4f4f4;
  --band-grey:#e9e9e9;
  --footer:#ececec;
  --footer-bar:#585858;
  --icon-grey:#dcdcdc;
  --icon-dark:#666;
}
*{box-sizing:border-box;margin:0;padding:0}
html,body{width:823px;height:1200px;overflow:hidden}
body{position:relative;background:#fff;font-family:'Open Sans',sans-serif;color:var(--ink)}
.abs{position:absolute}
.btn{position:absolute;display:block;background:var(--btn);color:#fff;font-size:8px;text-align:center;border-radius:2px;border-bottom:1px solid var(--btn-dark)}
p{line-height:1.6}

.topbar{left:0;top:0;width:823px;height:12px;background:#f3f3f3;border-bottom:1px solid #e2e2e2}
.topbar .phone{left:520px;top:1px;font-size:7px;color:var(--ink-soft)}
.topbar .social{top:2px;width:9px;height:8px;border-left:1px solid #ddd}
.topbar .social span{display:block;margin:1px 0 0 2px;width:5px;height:5px;border:1px solid #999;border-radius:50%}

.nav{left:0;top:12px;width:823px;height:41px;background:#fff}
.logo{left:155px;top:9px;font-size:17px;color:var(--accent);border-bottom:1px solid var(--accent);line-height:18px}
.menu a{position:absolute;top:16px;font-size:9.5px;color:var(--muted);text-decoration:none}
.menu a.current{color:#333;border-bottom:1px solid #333}
.login{left:576px;top:15px;width:43px;height:15px;line-height:14px;background:var(--green);border-bottom-color:#509620}
.signup{left:621px;top:15px;width:43px;height:15px;line-height:14px}

.hero{left:0;top:53px;width:823px;height:196px;background:repeating-linear-gradient(45deg,#3f3f3f 0 2px,#363636 2px 4px)}
.hero-foot{left:0;top:249px;width:823px;height:51px;background:linear-gradient(#e4e4e4,#f3f3f3)}
.hero h1{left:149px;top:48px;width:210px;font-size:14px;font-weight:400;color:#fff;line-height:16px}
.hero p{left:149px;top:86px;width:200px;font-size:9px;color:#eee;line-height:10.5px}
.hero .btn{left:150px;top:137px;width:59px;height:16px;line-height:15px}
.screen-main{left:351px;top:81px;width:286px;height:200px;border-radius:3px;background:linear-gradient(90deg,#2c2c2c 0 30%,#f1f1f1 30% 100%);box-shadow:0 6px 14px rgba(0,0,0,.3)}
.screen-back{left:634px;top:130px;width:67px;height:146px;background:linear-gradient(#d8d8d8,#bdbdbd);box-shadow:0 4px 10px rgba(0,0,0,.25)}

.services{left:0;top:300px;width:823px;height:218px;background:var(--band)}
.services h2{left:0;top:13px;width:823px;text-align:center;font-size:14px;font-weight:400;color:var(--accent)}
.services .lead{left:211px;top:31px;width:400px;text-align:center;font-size:8px;line-height:16px;color:var(--ink-soft)}
.svc{position:absolute;top:75px;width:120px;text-align:center}
.svc svg{display:block;margin:0 auto}
.svc h3{margin-top:10px;font-size:10.5px;font-weight:400;color:#555}
.svc.active h3{color:var(--accent)}
.svc p{margin-top:4px;font-size:7px;line-height:9.7px;color:var(--muted)}

.about{left:0;top:518px;width:823px;height:216px;background:var(--band-grey)}
.about h2{left:155px;top:16px;width:260px;font-size:14px;font-weight:400;color:#555;line-height:16px}
.about p{position:absolute;left:155px;width:295px;font-size:7.7px;line-height:13px;color:var(--ink-soft)}
.about .btn{left:155px;top:168px;width:59px;height:16px;line-height:15px}
.devices{left:470px;top:13px;width:173px;height:189px;border-radius:10px;background:linear-gradient(135deg,#f7f7f7,#cfcfcf)}

.seo{left:0;top:734px;width:823px;height:312px;background:#fff}
.seo h2{left:0;top:12px;width:823px;text-align:center;font-size:19px;font-weight:400;color:#555}
.seo .rule{left:330px;top:42px;width:163px;height:1px;background:#ccc}
.seo .lead{left:260px;top:46px;width:303px;text-align:center;font-size:9.3px;line-height:14px;color:var(--muted)}
.seo .divider{left:396px;top:89px;width:1px;height:201px;background:#ddd}
.item{position:absolute;width:190px}
.item h3{font-size:10px;font-weight:400;color:#444}
.item p{margin-top:5px;font-size:7.7px;line-height:11px;color:var(--muted)}
.item .btn{position:relative;margin-top:12px;width:59px;height:16px;line-height:15px}
.item-icon{position:absolute}

.footer{left:0;top:1046px;width:823px;height:128px;background:var(--footer)}
.fcol{position:absolute;top:19px}
.fcol h4{font-size:8px;font-weight:400;color:#555;padding-bottom:4px;border-bottom:1px solid #ddd}
.fcol h4 span{color:var(--accent)}
.fcol ul{list-style:none;margin-top:6px}
.fcol li{font-size:6.8px;line-height:13px;color:#555}
.fcol p{font-size:6.6px;line-height:10px;color:var(--muted);margin-top:6px}
.input{width:131px;height:17px;margin-top:7px;border:1px solid #bbb;background:#f7f7f7;font-size:6.5px;color:#999;padding:4px 5px}
.fcol .btn{position:relative;margin-top:9px;width:60px;height:16px;line-height:15px}
.socials{display:flex;margin-top:8px;border-left:1px solid #ccc}
.socials span{width:16px;height:12px;border-right:1px solid #ccc;display:flex;align-items:center;justify-content:center}
.socials i{display:block;width:6px;height:6px;border:1px solid #888;border-radius:50%}
.contact h5{margin-top:9px;font-size:7.5px;font-weight:400;color:var(--accent)}
.contact p{margin-top:1px;font-size:6.6px;line-height:9.5px;color:#666}
.bottom{left:0;top:1174px;width:823px;height:26px;background:var(--footer-bar)}
.bottom p{position:absolute;left:155px;top:7px;font-size:6.8px;color:#eee}
</style>
</head>
<body>

<header class="abs topbar">
  <span class="abs phone">&#9742; +00 5550 1234</span>
  <span class="abs social" style="left:588px"><span></span></span>
  <span class="abs social" style="left:604px"><span></span></span>
  <span class="abs social" style="left:620px"><span></span></span>
  <span class="abs social" style="left:636px"><span></span></span>
  <span class="abs social" style="left:652px"><span></span></span>
</header>

<nav class="abs nav">
  <div class="abs logo">Brivvora.example</div>
  <div class="menu">
    <a class="current" style="left:353px">Home</a>
    <a style="left:388px">Features</a>
    <a style="left:435px">Plans &amp; Pricing</a>
    <a style="left:508px">Blog</a>
    <a style="left:537px">Add-ons</a>
  </div>
  <a class="btn login">Log in</a>
  <a class="btn signup">Sign up</a>
</nav>

<section class="abs hero">
  <h1 class="abs">Lorem Ipsum is simply dummy text of the printing</h1>
  <p class="abs">Lorem Ipsum is simply dummy text of the printing and typesetting industry. Lorem Ipsum has been the industry's standard dummy text ever since the 1500s,</p>
  <a class="btn">Learn More</a>
  <div class="abs screen-back" role="img" aria-label="Second dashboard window behind the main preview"></div>
  <div class="abs screen-main" role="img" aria-label="Admin dashboard window preview with charts and forms"></div>
</section>
<div class="abs hero-foot"></div>

<section class="abs services">
  <h2 class="abs">The Services We Provide</h2>
  <p class="abs lead">Lorem Ipsum is simply dummy text of the printing and typesetting industry. Lorem Ipsum has been the industry's standard dummy text ever since the 1500s.</p>

  <div class="svc active" style="left:154px">
    <svg width="56" height="56" viewBox="0 0 56 56"><circle cx="28" cy="28" r="27" fill="none" stroke="var(--accent)" stroke-width="2"/><circle cx="28" cy="28" r="23" fill="var(--accent)"/><circle cx="28" cy="28" r="9" fill="#fff"/><path d="M28 28V21A7 7 0 0 1 35 28Z" fill="var(--accent)"/></svg>
    <h3>SERP Tracking</h3>
    <p>Lorem Ipsum is simply dummy text of the printing and typesetting industry. Lorem Ipsum has been the industry's standard dummy text ever since the 1500s,</p>
  </div>
  <div class="svc" style="left:283px">
    <svg width="56" height="56" viewBox="0 0 56 56"><circle cx="28" cy="28" r="23" fill="var(--icon-grey)"/><rect x="20" y="30" width="4" height="7" fill="var(--icon-dark)"/><rect x="26" y="25" width="4" height="12" fill="var(--icon-dark)"/><rect x="32" y="19" width="4" height="18" fill="var(--icon-dark)"/></svg>
    <h3>Link Analysis</h3>
    <p>Lorem Ipsum is simply dummy text of the printing and typesetting industry. Lorem Ipsum has been the industry's standard dummy text ever since the 1500s,</p>
  </div>
  <div class="svc" style="left:417px">
    <svg width="56" height="56" viewBox="0 0 56 56"><circle cx="28" cy="28" r="23" fill="var(--icon-grey)"/><path d="M17 37L23 29L28 32L35 22L39 25V37Z" fill="var(--icon-dark)"/></svg>
    <h3>TrustRank Scan</h3>
    <p>Lorem Ipsum is simply dummy text of the printing and typesetting industry. Lorem Ipsum has been the industry's standard dummy text ever since the 1500s,</p>
  </div>
  <div class="svc" style="left:548px">
    <svg width="56" height="56" viewBox="0 0 56 56"><circle cx="28" cy="28" r="23" fill="var(--icon-grey)"/><path d="M17 35L24 26L29 31L38 21M17 29L24 22L30 28L38 20" fill="none" stroke="var(--icon-dark)" stroke-width="2"/></svg>
    <h3>Track your Competition</h3>
    <p>Lorem Ipsum is simply dummy text of the printing and typesetting industry. Lorem Ipsum has been the industry's standard dummy text ever since the 1500s,</p>
  </div>
</section>

<section class="abs about">
  <h2 class="abs">Lorem Ipsum is simply dummy text of the printing</h2>
  <p style="top:62px">Lorem Ipsum is simply dummy text of the printing and typesetting industry. Lorem Ipsum has been the industry's standard dummy text ever since the 1500s, when an unknown printer took a galley of type and scrambled it to make a type specimen book.</p>
  <p style="top:122px">Lorem Ipsum is simply dummy text of the printing and typesetting industry. Lorem Ipsum has been the industry's standard dummy text ever since the 1500s,</p>
  <a class="btn">Learn More</a>
  <div class="abs devices" role="img" aria-label="Tablet and phone showing the dashboard"></div>
</section>

<section class="abs seo">
  <h2 class="abs">Our SEO Services</h2>
  <div class="abs rule"></div>
  <p class="abs lead">Lorem ipsum dolor sit amet, sed tellus tincidunt ad diam, nulla turpis, dolor ut pellentesque,</p>
  <div class="abs divider"></div>

  <svg class="item-icon" style="left:161px;top:90px" width="28" height="26" viewBox="0 0 28 26"><rect x="0" y="0" width="28" height="19" rx="1" fill="#8aa4c8"/><rect x="2" y="2" width="24" height="15" fill="#a9bfdc"/><rect x="12" y="19" width="4" height="4" fill="#666"/><rect x="7" y="23" width="14" height="2" fill="#555"/></svg>
  <div class="item" style="left:199px;top:90px">
    <h3>Link Building</h3>
    <p>Lorem ipsum dolor sit amet, sed tellus tincidunt ad diam, nulla turpis, dolor ut pellentesque,</p>
    <a class="btn">Reade More</a>
  </div>

  <svg class="item-icon" style="left:418px;top:92px" width="32" height="28" viewBox="0 0 32 28"><path d="M0 14L31 1L20 27L15 17Z" fill="#2fb6b0"/><path d="M15 17L31 1L13 25Z" fill="#1e8f8a"/></svg>
  <div class="item" style="left:460px;top:90px">
    <h3>Social Networking</h3>
    <p>Lorem ipsum dolor sit amet, sed tellus tincidunt ad diam, nulla turpis, dolor ut pellentesque,</p>
    <a class="btn">Reade More</a>
  </div>

  <div class="item-icon" style="left:161px;top:188px;width:28px;height:28px;border-radius:4px;background:linear-gradient(#e58a3a 0 45%,#3bb3a7 45%)" role="img" aria-label="Writer avatar icon"></div>
  <div class="item" style="left:199px;top:188px">
    <h3>Article Submission and Writing</h3>
    <p>Lorem ipsum dolor sit amet, sed tellus tincidunt ad diam, nulla turpis, dolor ut pellentesque,</p>
    <a class="btn">Reade More</a>
  </div>

  <svg class="item-icon" style="left:422px;top:186px" width="30" height="30" viewBox="0 0 30 30"><rect x="8" y="0" width="22" height="16" rx="2" fill="#f0a11f"/><rect x="0" y="6" width="22" height="16" rx="2" fill="#2a8fd6"/><path d="M4 22V29L11 22Z" fill="#2a8fd6"/><circle cx="6" cy="14" r="1.5" fill="#fff"/><circle cx="11" cy="14" r="1.5" fill="#fff"/><circle cx="16" cy="14" r="1.5" fill="#fff"/></svg>
  <div class="item" style="left:460px;top:188px;width:210px">
    <h3>Social Bookmarking and Directory Submission</h3>
    <p style="width:190px">Lorem ipsum dolor sit amet, sed tellus tincidunt ad diam, nulla turpis, dolor ut pellentesque,</p>
    <a class="btn">Reade More</a>
  </div>
</section>

<footer class="abs footer">
  <div class="fcol" style="left:153px;width:118px">
    <h4>About <span>Brivvora.example</span></h4>
    <ul><li>Home</li><li>Features</li><li>Plans &amp; Pricing</li><li>Blog</li><li>Add-ons</li></ul>
  </div>
  <div class="fcol" style="left:286px;width:76px">
    <h4>Support</h4>
    <ul><li>Support &amp; FAQ</li><li>About Us</li><li>Jobs</li><li>SEO/SEM Knowledge Base</li></ul>
  </div>
  <div class="fcol" style="left:378px;width:140px">
    <h4>NEWSLETTER</h4>
    <p>Subscribe to our newsletter! Get productivity tips, product updates and special offers.</p>
    <div class="input">Your Email Address</div>
    <a class="btn">Subscribe</a>
  </div>
  <div class="fcol contact" style="left:548px;width:120px">
    <h4>STAY IN TOUCH</h4>
    <div class="socials"><span><i></i></span><span><i></i></span><span><i></i></span><span><i></i></span></div>
    <h5>Contact us</h5>
    <p>Lindenweg 12<br>40-118 Marrowford<br>US: +1 (555) 014 2288</p>
  </div>
</footer>
<div class="abs bottom"><p>Copyright © 2013. Brivvora.example</p></div>

</body>
</html>
```